Childcare Centre Franchise Website Design

Our business is Childcare centre, and we are the franchise with 4 centres currently, we would like to have the website similar as the link below,
https://www.maplewren.edu.au/
with the same items, functions and pages. Locations information for all centres, and have pages for each centre. Additionally, we will need a page for online enrolment.
Our logo is attached.

```html
<!DOCTYPE html>
<html lang="en">
<head>
<meta charset="utf-8">
<title>Little Acorns Childcare &amp; Education – Home</title>
<link href="https://fonts.googleapis.com/css2?family=Merriweather:wght@700;900&family=Lato:wght@400;700;900&display=swap" rel="stylesheet">
<style>
:root{
  --board:#eef0f2;
  --teal:#1a9d93;
  --teal-dark:#137e76;
  --maroon:#7a2b2b;
  --green:#6aae3f;
  --pink:#e2477a;
  --brown:#6b3a28;
  --orange:#f26a35;
  --beige:#f7efe3;
  --ink:#2b2b2b;
  --muted:#6d6d6d;
  --footer:#1c100b;
  --white:#ffffff;
}
*{box-sizing:border-box;margin:0;padding:0}
html,body{width:1200px;height:4312px;overflow:hidden;background:var(--board)}
body{position:relative;font-family:'Lato',sans-serif;color:var(--ink)}
h1,h2,h3,.serif{font-family:'Merriweather',serif}
.board{position:absolute;background:var(--white);overflow:hidden;box-shadow:0 2px 10px rgba(0,0,0,.08)}
.desk{left:80px;top:40px;width:740px;height:2680px}
.mob{left:912px;top:60px;width:220px;height:4220px}
.photo{background:linear-gradient(135deg,#e9c9a3,#c98a5a 55%,#7fb0c4)}
.photo.b{background:linear-gradient(135deg,#f3d36b,#e07a4f 50%,#5aa0c8)}
.photo.c{background:linear-gradient(135deg,#b9d98a,#e8b07a 60%,#8a5a3a)}
.photo.d{background:linear-gradient(135deg,#f0a5b5,#f6d38a 55%,#76b3a0)}
.btn{display:inline-flex;align-items:center;gap:4px;border:1.5px solid var(--green);color:var(--green);border-radius:20px;font-weight:700;background:var(--white);white-space:nowrap}
.btn svg{width:9px;height:9px}
.row{display:flex}
.center{text-align:center}
.hl-m{color:var(--maroon)}
.hl-t{color:var(--teal)}
.logo{display:flex;align-items:center;gap:8px}
.logo-dot{border-radius:50%;background:var(--green)}
.logo-name{font-family:'Merriweather',serif;font-weight:900;color:var(--maroon);line-height:1}

/* ---------- desktop ---------- */
.d-header{height:110px;position:relative;padding:20px 26px 0}
.d-header .logo-dot{width:40px;height:40px}
.d-header .logo-name{font-size:15px}
.d-header .logo small{display:block;font-family:'Lato',sans-serif;font-size:7px;color:var(--teal);letter-spacing:1px;margin-top:3px;font-weight:700}
.d-search{position:absolute;left:240px;top:28px;width:200px;height:22px;border:1px solid #ddd;border-radius:12px;font-size:7px;color:#999;padding:6px 10px}
.d-search-go{position:absolute;left:446px;top:28px;width:22px;height:22px;border-radius:50%;background:var(--teal)}
.d-phone{position:absolute;left:482px;top:27px;display:flex;gap:5px;align-items:center}
.d-phone .ico{width:22px;height:22px;border-radius:50%;background:var(--maroon);display:flex;align-items:center;justify-content:center}
.d-phone span{font-size:6px;color:var(--muted);display:block}
.d-phone b{font-size:9px;color:var(--maroon)}
.d-enrol{position:absolute;left:610px;top:28px;height:22px;padding:0 12px;border-radius:12px;background:var(--orange);color:var(--white);font-size:7px;font-weight:900;display:flex;align-items:center}
.d-nav{position:absolute;left:0;right:0;bottom:0;height:20px;background:var(--teal);display:flex;justify-content:center;gap:22px;align-items:center}
.d-nav a{color:var(--white);font-size:7px;font-weight:700;text-decoration:none;letter-spacing:.4px}
.d-hero{height:420px;position:relative}
.d-hero .text{position:absolute;left:60px;top:120px;color:var(--white)}
.d-hero .text p{font-size:13px;font-weight:700;letter-spacing:1px}
.d-hero h1{font-size:30px;font-weight:900;line-height:1.1}
.d-hero .sub{font-size:12px;letter-spacing:2px;margin:4px 0 16px}
.d-hero .btn{background:var(--green);color:var(--white);font-size:8px;padding:6px 14px;border-color:var(--green)}
.d-support{height:350px;padding:40px 120px 0}
.d-support h2,.d-learn h2,.d-news h2{font-size:15px;text-align:center;text-transform:uppercase}
.d-support .cols{display:flex;justify-content:space-between;margin-top:40px}
.d-support .col{width:140px;text-align:center}
.icon-circ{width:46px;height:46px;margin:0 auto 10px;display:block}
.d-support h3{font-family:'Lato',sans-serif;font-size:9px;font-weight:900;margin-bottom:6px}
.d-support p{font-size:7px;color:var(--muted);line-height:1.5;margin-bottom:12px}
.d-support .btn{font-size:7px;padding:4px 12px}
.d-learn{height:360px;background:var(--beige);padding:44px 120px 0}
.d-learn h2{line-height:1.5}
.d-learn .cols{display:flex;justify-content:space-between;margin-top:30px}
.d-learn .item{width:112px;text-align:center}
.d-learn .circ{width:104px;height:104px;border-radius:50%;border:4px solid var(--white);margin:0 auto 10px}
.d-learn .item p{font-size:8px;font-weight:700}
.d-news{height:430px;padding:40px 100px 0}
.d-news .cards{display:flex;justify-content:space-between;margin-top:30px}
.card{width:170px;border-radius:8px;overflow:hidden;color:var(--white)}
.card .img{height:110px;border:4px solid currentColor}
.card.pink{background:var(--pink)}.card.brown{background:var(--brown)}.card.orange{background:var(--orange)}
.card .body{padding:10px 12px 14px}
.card .date{display:inline-block;background:var(--white);color:var(--ink);font-size:6px;padding:2px 6px;border-radius:8px;margin-bottom:8px}
.card h3{font-size:9px;line-height:1.3;margin-bottom:6px}
.card p{font-size:6.5px;line-height:1.5;margin-bottom:10px;opacity:.95}
.card .more{font-size:7px;font-weight:900}
.d-village{height:380px;background:var(--teal);padding:36px 70px 0;position:relative;color:var(--white)}
.d-village h2{font-size:15px;text-align:center;line-height:1.5}
.d-village .states{display:flex;justify-content:space-between;margin-top:24px}
.state{width:170px}
.state h3{font-family:'Lato',sans-serif;font-size:9px;margin-bottom:10px}
.centres{display:grid;grid-template-columns:1fr 1fr;gap:8px}
.centre{display:flex;align-items:center;gap:4px;background:var(--white);border-radius:16px;padding:3px;color:var(--ink);font-size:5.5px;line-height:1.3}
.centre i{flex:none;width:22px;height:22px;border-radius:50%}
.state .btn{margin-top:16px;font-size:6.5px;padding:4px 10px;background:var(--white)}
.arrow{position:absolute;top:200px;width:18px;height:18px;border-radius:50%;background:var(--white);display:flex;align-items:center;justify-content:center}
.d-bold{height:320px;position:relative}
.d-bold .circ{position:absolute;left:140px;top:70px;width:180px;height:180px;border-radius:50%;border:6px solid var(--teal)}
.d-bold .text{position:absolute;left:370px;top:110px;width:260px}
.kicker{color:var(--orange);font-family:'Merriweather',serif;font-weight:900;font-size:13px}
.d-bold h2{color:var(--teal);font-size:14px;line-height:1.35;margin:4px 0 8px}
.d-bold p{font-size:7px;color:var(--muted);margin-bottom:12px}
.d-bold .btn{font-size:7px;padding:4px 12px}
.d-footer{height:240px;background:var(--footer);color:#cfc7c2;position:relative;padding:40px 70px 0}
.d-footer .logo-dot{width:36px;height:36px}
.d-footer .logo-name{font-size:14px;color:var(--white)}
.d-footer .fphone{display:flex;gap:6px;align-items:center;margin-top:24px;color:var(--white);font-weight:900;font-size:9px}
.fphone i{width:18px;height:18px;border-radius:50%;background:var(--maroon);display:flex;align-items:center;justify-content:center}
.d-footer .cols{position:absolute;left:300px;top:40px;display:flex;gap:50px}
.fcol h4{color:var(--white);font-size:7.5px;margin-bottom:8px}
.fcol a{display:block;color:#cfc7c2;font-size:6.5px;text-decoration:none;margin-bottom:6px}
.d-footer .copy{position:absolute;left:0;right:0;bottom:0;height:26px;border-top:1px solid #3a2a22;font-size:6.5px;display:flex;align-items:center;justify-content:center}

/* ---------- mobile ---------- */
.m-top{height:14px;background:var(--teal)}
.m-head{height:38px;display:flex;align-items:center;justify-content:space-between;padding:0 10px}
.m-head .logo-dot{width:20px;height:20px}
.m-head .logo-name{font-size:8px}
.m-burger{width:16px;height:12px;border-top:2px solid var(--maroon);border-bottom:2px solid var(--maroon);position:relative}
.m-burger:after{content:"";position:absolute;left:0;right:0;top:3px;border-top:2px solid var(--maroon)}
.m-hero{height:88px;position:relative}
.m-hero .text{position:absolute;left:12px;top:26px;color:var(--white)}
.m-hero p{font-size:6px;font-weight:700}
.m-hero h1{font-size:11px}
.m-support{height:700px;padding:26px 24px 0;text-align:center}
.m-support h2,.m-learn h2,.m-news h2{font-size:10px;line-height:1.45;text-transform:uppercase}
.m-support .col{margin-top:34px}
.m-support .icon-circ{width:52px;height:52px}
.m-support h3{font-family:'Lato',sans-serif;font-size:9px;margin-bottom:6px}
.m-support p{font-size:7px;color:var(--muted);line-height:1.5;margin-bottom:10px}
.m-support .btn{font-size:7px;padding:4px 12px}
.m-learn{height:780px;background:var(--beige);padding:24px 24px 0;text-align:center}
.m-learn .item{margin-top:22px}
.m-learn .circ{width:130px;height:130px;border-radius:50%;border:4px solid var(--white);margin:0 auto 8px}
.m-learn p{font-size:8px;font-weight:700}
.m-news{height:820px;padding:24px 24px 0;text-align:center}
.m-news .card{width:172px;margin:18px auto 0;text-align:left}
.m-news .card .img{height:86px}
.m-village{height:750px;background:var(--teal);padding:22px 22px 0;color:var(--white)}
.m-village h2{font-size:10px;text-align:center;line-height:1.45;margin-bottom:14px}
.m-village .state{width:auto;margin-bottom:18px}
.m-village .centres{gap:6px}
.m-village .btn{margin-top:10px}
.m-bold{height:370px;padding:24px 26px 0}
.m-bold .circ{width:150px;height:150px;border-radius:50%;border:5px solid var(--teal);margin:0 auto 18px}
.m-bold .kicker{font-size:10px}
.m-bold h2{color:var(--teal);font-size:10px;line-height:1.4;margin:4px 0 8px}
.m-bold p{font-size:7px;color:var(--muted);margin-bottom:10px}
.m-bold .btn{font-size:7px;padding:4px 12px}
.m-footer{height:660px;background:var(--footer);color:#cfc7c2;padding:26px 20px 0;position:relative}
.m-footer .logo{flex-direction:column;gap:6px}
.m-footer .logo-dot{width:40px;height:40px}
.m-footer .logo-name{color:var(--white);font-size:12px}
.m-footer .fphone{display:flex;gap:6px;align-items:center;margin:20px 0;color:var(--white);font-weight:900;font-size:9px}
.m-footer .fcol{margin-bottom:16px}
.m-footer .copy{position:absolute;left:0;right:0;bottom:0;height:24px;border-top:1px solid #3a2a22;font-size:5.5px;display:flex;align-items:center;justify-content:center}
</style>
</head>
<body>

<!-- ================= Desktop ================= -->
<div class="board desk">
  <header class="d-header">
    <div class="logo"><span class="logo-dot"></span><div><div class="logo-name">LITTLE ACORNS</div><small>CHILDCARE &amp; EDUCATION</small></div></div>
    <div class="d-search">Search…</div>
    <div class="d-search-go"></div>
    <div class="d-phone"><span class="ico"><svg width="10" height="10" viewBox="0 0 24 24" fill="#fff"><path d="M6.6 10.8a15.1 15.1 0 0 0 6.6 6.6l2.2-2.2c.3-.3.7-.4 1-.2 1.1.4 2.3.6 3.6.6.6 0 1 .4 1 1V20c0 .6-.4 1-1 1A17 17 0 0 1 3 4c0-.6.4-1 1-1h3.5c.6 0 1 .4 1 1 0 1.3.2 2.5.6 3.6.1.3 0 .7-.2 1z"/></svg></span><div><span>Call Us</span><b>1300 000 000</b></div></div>
    <div class="d-enrol">ENROL NOW</div>
    <nav class="d-nav"><a>FIND A CHILDCARE CENTRE</a><a>CHILDCARE OPTIONS</a><a>CHILDCARE CENTRES</a><a>PROGRAMS</a><a>ABOUT US</a><a>CONTACT</a></nav>
  </header>

  <section class="d-hero photo" role="img" aria-label="Educator playing with a young child at a table of colourful toys">
    <div class="text"><p>WELCOME TO</p><h1>LITTLE ACORNS</h1><div class="sub">CHILDCARE &amp; EDUCATION</div><span class="btn">FIND A CENTRE NEAR YOU <svg viewBox="0 0 10 10"><path d="M3 1l4 4-4 4" stroke="#fff" stroke-width="1.6" fill="none"/></svg></span></div>
  </section>

  <section class="d-support">
    <h2><span class="hl-m">We're here to support</span> <span class="hl-t">the whole family</span></h2>
    <div class="cols">
      <div class="col"><svg class="icon-circ" viewBox="0 0 46 46"><path d="M9 22L23 10l14 12v14H9z" fill="none" stroke="var(--maroon)" stroke-width="2.5"/><circle cx="23" cy="27" r="5" fill="var(--teal)"/></svg><h3>Child Care Subsidy</h3><p>Lorem ipsum dolor sit amet consectetur adipiscing, sed eiusmod tempor incididunt ut labore et dolore magna aliqua.</p><span class="btn">Read More <svg viewBox="0 0 10 10"><path d="M3 1l4 4-4 4" stroke="var(--green)" stroke-width="1.6" fill="none"/></svg></span></div>
      <div class="col"><svg class="icon-circ" viewBox="0 0 46 46"><circle cx="23" cy="17" r="8" fill="none" stroke="var(--maroon)" stroke-width="2.5"/><path d="M9 40c2-9 8-12 14-12s12 3 14 12" fill="none" stroke="var(--teal)" stroke-width="2.5"/></svg><h3>Why Maplewren?</h3><p>Lorem ipsum dolor sit amet consectetur adipiscing, sed eiusmod tempor incididunt ut labore et dolore magna aliqua.</p><span class="btn">Read More <svg viewBox="0 0 10 10"><path d="M3 1l4 4-4 4" stroke="var(--green)" stroke-width="1.6" fill="none"/></svg></span></div>
      <div class="col"><svg class="icon-circ" viewBox="0 0 46 46"><path d="M23 38S8 28 8 17a7.5 7.5 0 0 1 15-1 7.5 7.5 0 0 1 15 1c0 11-15 21-15 21z" fill="none" stroke="var(--maroon)" stroke-width="2.5"/><path d="M23 19v10M18 24h10" stroke="var(--teal)" stroke-width="2.5"/></svg><h3>Health &amp; Wellbeing</h3><p>Lorem ipsum dolor sit amet consectetur adipiscing, sed eiusmod tempor incididunt ut labore et dolore magna aliqua.</p><span class="btn">Read More <svg viewBox="0 0 10 10"><path d="M3 1l4 4-4 4" stroke="var(--green)" stroke-width="1.6" fill="none"/></svg></span></div>
    </div>
  </section>

  <section class="d-learn">
    <h2><span class="hl-m">A love of learning. Confidence. Curiosity.</span><br><span class="hl-t">Here are some of the ways we help<br>children thrive.</span></h2>
    <div class="cols">
      <div class="item"><div class="circ photo" role="img" aria-label="Child building with blocks"></div><p>Lorem ipsum dolor sit</p></div>
      <div class="item"><div class="circ photo b" role="img" aria-label="Children painting"></div><p>Lorem ipsum dolor sit</p></div>
      <div class="item"><div class="circ photo c" role="img" aria-label="Toddler playing outdoors"></div><p>Lorem ipsum dolor sit</p></div>
      <div class="item"><div class="circ photo d" role="img" aria-label="Child with educator reading"></div><p>Lorem ipsum dolor sit</p></div>
    </div>
  </section>

  <section class="d-news">
    <h2><span class="hl-m">Latest news &amp; advice from</span> <span class="hl-t">our team of experts</span></h2>
    <div class="cards">
      <article class="card pink"><div class="img photo b" role="img" aria-label="Children playing with toys"></div><div class="body"><span class="date">May 12, 2021</span><h3>Lorem ipsum dolor sit amet elit</h3><p>Sed do eiusmod tempor incididunt ut labore dolore magna.</p><span class="more">READ MORE ›</span></div></article>
      <article class="card brown"><div class="img photo" role="img" aria-label="Educator with toddlers"></div><div class="body"><span class="date">May 12, 2021</span><h3>Lorem ipsum dolor sit amet elit</h3><p>Sed do eiusmod tempor incididunt ut labore dolore magna.</p><span class="more">READ MORE ›</span></div></article>
      <article class="card orange"><div class="img photo c" role="img" aria-label="Child drawing at a desk"></div><div class="body"><span class="date">May 12, 2021</span><h3>Lorem ipsum dolor sit amet elit</h3><p>Sed do eiusmod tempor incididunt ut labore dolore magna.</p><span class="more">READ MORE ›</span></div></article>
    </div>
  </section>

  <section class="d-village">
    <h2>FIND YOUR VILLAGE<br>CHILDCARE CENTRES BY STATE</h2>
    <span class="arrow" style="left:30px"><svg width="8" height="8" viewBox="0 0 10 10"><path d="M7 1L3 5l4 4" stroke="var(--teal)" stroke-width="1.8" fill="none"/></svg></span>
    <span class="arrow" style="right:30px"><svg width="8" height="8" viewBox="0 0 10 10"><path d="M3 1l4 4-4 4" stroke="var(--teal)" stroke-width="1.8" fill="none"/></svg></span>
    <div class="states">
      <div class="state"><h3>Queensland</h3><div class="centres"><div class="centre"><i class="photo"></i>Maplewren Childcare &amp; Education Brookfield</div><div class="centre"><i class="photo b"></i>Maplewren Childcare &amp; Education Redcliffe</div><div class="centre"><i class="photo c"></i>Maplewren Childcare &amp; Education Albany Creek</div><div class="centre"><i class="photo d"></i>Maplewren Childcare &amp; Education Hillcrest</div></div><span class="btn">VIEW ALL QLD CENTRES ›</span></div>
      <div class="state"><h3>South Australia</h3><div class="centres"><div class="centre"><i class="photo b"></i>Maplewren Childcare &amp; Education Glenelg</div><div class="centre"><i class="photo"></i>Maplewren Childcare &amp; Education Norwood</div><div class="centre"><i class="photo d"></i>Maplewren Childcare &amp; Education Unley Park</div><div class="centre"><i class="photo c"></i>Maplewren Childcare &amp; Education Prospect</div></div><span class="btn">VIEW ALL SA CENTRES ›</span></div>
      <div class="state"><h3>Victoria</h3><div class="centres"><div class="centre"><i class="photo c"></i>Maplewren Childcare &amp; Education Kew</div><div class="centre"><i class="photo d"></i>Maplewren Childcare &amp; Education Geelong</div><div class="centre"><i class="photo"></i>Maplewren Childcare &amp; Education Box Hill</div><div class="centre"><i class="photo b"></i>Maplewren Childcare &amp; Education Richmond</div></div><span class="btn">VIEW ALL VIC CENTRES ›</span></div>
    </div>
  </section>

  <section class="d-bold">
    <div class="circ photo c" role="img" aria-label="Educators and children gathered outdoors"></div>
    <div class="text"><div class="kicker">BE BOLD</div><h2>CHILDCARE IS MORE THAN A CAREER AT MAPLEWREN</h2><p>Lorem ipsum dolor sit amet consectetur, sed do eiusmod tempor.</p><span class="btn">CAREERS AT MAPLEWREN ›</span></div>
  </section>

  <footer class="d-footer">
    <div class="logo"><span class="logo-dot"></span><span class="logo-name">LITTLE ACORNS</span></div>
    <div class="fphone"><i><svg width="9" height="9" viewBox="0 0 24 24" fill="#fff"><path d="M6.6 10.8a15.1 15.1 0 0 0 6.6 6.6l2.2-2.2c.3-.3.7-.4 1-.2 1.1.4 2.3.6 3.6.6.6 0 1 .4 1 1V20c0 .6-.4 1-1 1A17 17 0 0 1 3 4c0-.6.4-1 1-1h3.5c.6 0 1 .4 1 1 0 1.3.2 2.5.6 3.6.1.3 0 .7-.2 1z"/></svg></i>1300 000 000</div>
    <div class="cols">
      <div class="fcol"><h4>Find Your Closest Centre</h4><a>Childcare NSW</a><a>Childcare VIC</a><a>Childcare QLD</a><a>Childcare SA</a><a>Childcare ACT</a></div>
      <div class="fcol"><h4>Childcare and Education</h4><a>Employer Sponsored Care</a><a>Parental Information</a><a>News &amp; Advice</a><a>Our Brand Story</a><a>FAQs</a></div>
      <div class="fcol"><h4>Careers at Maplewren</h4><a>Become a Centre Manager</a><a>Contact Us</a><a>Feedback</a><a>Enrol Online</a><a>Sign up to MaplePlay</a></div>
    </div>
    <div class="copy">© Copyright 2021 Little Acorns Childcare | All Rights Reserved</div>
  </footer>
</div>

<!-- ================= Mobile ================= -->
<div class="board mob">
  <div class="m-top"></div>
  <div class="m-head"><div class="logo"><span class="logo-dot"></span><span class="logo-name">LITTLE ACORNS</span></div><span class="m-burger"></span></div>
  <section class="m-hero photo" role="img" aria-label="Educator playing with a young child"><div class="text"><p>WELCOME TO</p><h1>LITTLE ACORNS</h1></div></section>

  <section class="m-support">
    <h2><span class="hl-m">We're here to support</span><br><span class="hl-t">the whole family</span></h2>
    <div class="col"><svg class="icon-circ" viewBox="0 0 46 46"><path d="M9 22L23 10l14 12v14H9z" fill="none" stroke="var(--maroon)" stroke-width="2.5"/><circle cx="23" cy="27" r="5" fill="var(--teal)"/></svg><h3>Child Care Subsidy</h3><p>Lorem ipsum dolor sit amet consectetur adipiscing, sed eiusmod tempor incididunt ut labore et dolore.</p><span class="btn">Read More ›</span></div>
    <div class="col"><svg class="icon-circ" viewBox="0 0 46 46"><circle cx="23" cy="17" r="8" fill="none" stroke="var(--maroon)" stroke-width="2.5"/><path d="M9 40c2-9 8-12 14-12s12 3 14 12" fill="none" stroke="var(--teal)" stroke-width="2.5"/></svg><h3>Why Maplewren?</h3><p>Lorem ipsum dolor sit amet consectetur adipiscing, sed eiusmod tempor incididunt ut labore et dolore.</p><span class="btn">Read More ›</span></div>
    <div class="col"><svg class="icon-circ" viewBox="0 0 46 46"><path d="M23 38S8 28 8 17a7.5 7.5 0 0 1 15-1 7.5 7.5 0 0 1 15 1c0 11-15 21-15 21z" fill="none" stroke="var(--maroon)" stroke-width="2.5"/><path d="M23 19v10M18 24h10" stroke="var(--teal)" stroke-width="2.5"/></svg><h3>Health &amp; Wellbeing</h3><p>Lorem ipsum dolor sit amet consectetur adipiscing, sed eiusmod tempor incididunt ut labore et dolore.</p><span class="btn">Read More ›</span></div>
  </section>

  <section class="m-learn">
    <h2><span class="hl-m">A love of learning. Confidence. Curiosity.</span><br><span class="hl-t">Here are some of the ways we help children thrive.</span></h2>
    <div class="item"><div class="circ photo" role="img" aria-label="Child building with blocks"></div><p>Lorem ipsum dolor sit</p></div>
    <div class="item"><div class="circ photo b" role="img" aria-label="Children painting"></div><p>Lorem ipsum dolor sit</p></div>
    <div class="item"><div class="circ photo c" role="img" aria-label="Toddler playing outdoors"></div><p>Lorem ipsum dolor sit</p></div>
    <div class="item"><div class="circ photo d" role="img" aria-label="Child with educator reading"></div><p>Lorem ipsum dolor sit</p></div>
  </section>

  <section class="m-news">
    <h2><span class="hl-m">Latest news &amp; advice from</span><br><span class="hl-t">our team of experts</span></h2>
    <article class="card pink"><div class="img photo b" role="img" aria-label="Children playing with toys"></div><div class="body"><span class="date">May 12, 2021</span><h3>Lorem ipsum dolor sit amet elit</h3><p>Sed do eiusmod tempor incididunt ut labore dolore magna.</p><span class="more">READ MORE ›</span></div></article>
    <article class="card brown"><div class="img photo" role="img" aria-label="Educator with toddlers"></div><div class="body"><span class="date">May 12, 2021</span><h3>Lorem ipsum dolor sit amet elit</h3><p>Sed do eiusmod tempor incididunt ut labore dolore magna.</p><span class="more">READ MORE ›</span></div></article>
    <article class="card orange"><div class="img photo c" role="img" aria-label="Child drawing at a desk"></div><div class="body"><span class="date">May 12, 2021</span><h3>Lorem ipsum dolor sit amet elit</h3><p>Sed do eiusmod tempor incididunt ut labore dolore magna.</p><span class="more">READ MORE ›</span></div></article>
  </section>

  <section class="m-village">
    <h2>FIND YOUR VILLAGE<br>CHILDCARE CENTRES BY STATE</h2>
    <div class="state"><h3>Queensland</h3><div class="centres"><div class="centre"><i class="photo"></i>Maplewren Childcare &amp; Education Brookfield</div><div class="centre"><i class="photo b"></i>Maplewren Childcare &amp; Education Redcliffe</div><div class="centre"><i class="photo c"></i>Maplewren Childcare &amp; Education Albany Creek</div><div class="centre"><i class="photo d"></i>Maplewren Childcare &amp; Education Hillcrest</div></div><span class="btn">VIEW ALL QLD CENTRES ›</span></div>
    <div class="state"><h3>South Australia</h3><div class="centres"><div class="centre"><i class="photo b"></i>Maplewren Childcare &amp; Education Glenelg</div><div class="centre"><i class="photo"></i>Maplewren Childcare &amp; Education Norwood</div><div class="centre"><i class="photo d"></i>Maplewren Childcare &amp; Education Unley Park</div><div class="centre"><i class="photo c"></i>Maplewren Childcare &amp; Education Prospect</div></div><span class="btn">VIEW ALL SA CENTRES ›</span></div>
    <div class="state"><h3>Victoria</h3><div class="centres"><div class="centre"><i class="photo c"></i>Maplewren Childcare &amp; Education Kew</div><div class="centre"><i class="photo d"></i>Maplewren Childcare &amp; Education Geelong</div><div class="centre"><i class="photo"></i>Maplewren Childcare &amp; Education Box Hill</div><div class="centre"><i class="photo b"></i>Maplewren Childcare &amp; Education Richmond</div></div><span class="btn">VIEW ALL VIC CENTRES ›</span></div>
  </section>

  <section class="m-bold">
    <div class="circ photo c" role="img" aria-label="Educators and children gathered outdoors"></div>
    <div class="kicker">BE BOLD</div><h2>CHILDCARE IS MORE THAN A CAREER AT MAPLEWREN</h2><p>Lorem ipsum dolor sit amet consectetur, sed do eiusmod tempor.</p><span class="btn">CAREERS ›</span>
  </section>

  <footer class="m-footer">
    <div class="logo"><span class="logo-dot"></span><span class="logo-name">LITTLE ACORNS</span></div>
    <div class="fphone"><i><svg width="9" height="9" viewBox="0 0 24 24" fill="#fff"><path d="M6.6 10.8a15.1 15.1 0 0 0 6.6 6.6l2.2-2.2c.3-.3.7-.4 1-.2 1.1.4 2.3.6 3.6.6.6 0 1 .4 1 1V20c0 .6-.4 1-1 1A17 17 0 0 1 3 4c0-.6.4-1 1-1h3.5c.6 0 1 .4 1 1 0 1.3.2 2.5.6 3.6.1.3 0 .7-.2 1z"/></svg></i>1300 000 000</div>
    <div class="fcol"><h4>Find Your Closest Centre</h4><a>Childcare NSW</a><a>Childcare VIC</a><a>Childcare QLD</a><a>Childcare SA</a><a>Childcare ACT</a></div>
    <div class="fcol"><h4>Childcare and Education</h4><a>Employer Sponsored Care</a><a>Parental Information</a><a>News &amp; Advice</a><a>Our Brand Story</a><a>FAQs</a></div>
    <div class="fcol"><h4>Careers at Maplewren</h4><a>Become a Centre Manager</a><a>Contact Us</a><a>Feedback</a><a>Enrol Online</a><a>Sign up to MaplePlay</a></div>
    <div class="copy">© Copyright 2021 Little Acorns Childcare | All Rights Reserved</div>
  </footer>
</div>

</body>
</html>
```